Flyer Design for a Boston Therapeutic Clinic

I am a body therapist who needs a couple of flyers designed:
1. To fit half a page.
2. To fit a 5 inch by 3.5 inch flyer.
My practice is based in Boston, MA and my web site is:
www.LarchTessvik.Com
For the First half page:
A. Have my company's name and color shown as it appears on my web site (Larch Tessvik)
B. Have the following text: "Control your weight (This part should be emphasized) by balancing your nervous and digestive system through the Tessvik Method. The Tessvik Method, a technique developed by Dr. Mara. Tessvik, uses physical pressure to manipulate visceral tissue to bring back resiliency and proper functioning of the whole body."
Also helps with
-Constipation
-Bloating
-IBS
-eating disorders and overeating
Our practitioner is highly experienced. Please visit our web sites for reviews.
C. I would like to have a nice earthy feeling, something that feels "freeing" like open flowers, or an open land scape such as mountains or fields.
D. I also like the color blue, white, orange; perhaps if these colors can be integrated into the flyer, that would be great.
E. "Visit our web site LarchTessvik.com or call 786-555-0148"
The Smaller Flyer :
A.The smaller Flyer should also have my Company's name as shown on my web site (Larch Tessvik)
B.The following text: " Restore your body's natural resiliency and greatly reduce your physical pain through the Dr. Mara Tessvik Method of Structural Integration."
C. "Our practitioner is highly experienced and has a great reputation; visit our web site for reviews."
"Benefits:
"reduce aches and pains
reduce joint pain
reduce chronic muscular tension"
D, "feel better after the first session!"
E. if you could use a picture of me working on someone from my web site, that would be great.
F. I also like the colors white, orange and silver, for this one.
G. "Visit our web site LarchTessvik.com or call 786-555 0148"
I am very open minded,
I would like the flyer to evoke a sense of tranquility, professionalism, and simplicity. So if you have another angle you think would look good, then go for it! As long as it looks clean, professional and helpful.
Thanks a lot!
If you need any pictures from my web site, I have the original high resolution files that i can send.
Professionals and working men and women from ages 20-70
Clinic

```html
<!DOCTYPE html>
<html lang="en">
<head>
<meta charset="utf-8">
<title>Larch Tessvik Therapy – Flyers</title>
<link rel="stylesheet" href="https://fonts.googleapis.com/css2?family=PT+Sans:wght@400;700&family=Arimo:wght@400;700&family=Roboto+Condensed:ital,wght@0,700;1,700&display=swap">
<style>
  :root{
    --orange:#ee8421;
    --orange-deep:#e2701a;
    --tan:#cfb58c;
    --tan-light:#ecdfc7;
    --silver:#dcdcdc;
    --ink:#1b1b1b;
    --navy:#2b3690;
    --bullet:#e02027;
    --page:#f2f0ec;
    --white:#ffffff;
  }
  *{box-sizing:border-box;margin:0;padding:0}
  html,body{width:1200px;height:1200px;overflow:hidden;background:var(--page)}
  body{position:relative;font-family:"PT Sans",sans-serif;color:var(--ink)}

  .flyer{position:absolute;background:var(--white);overflow:hidden;box-shadow:0 3px 10px rgba(0,0,0,.18)}
  .flyer svg.backdrop{position:absolute;left:0;top:0}
  .abs{position:absolute}
  .photo{position:absolute}
  .brand-name{font-family:"PT Sans",sans-serif;font-weight:400;color:var(--orange-deep);white-space:nowrap;letter-spacing:.5px}

  /* small flyer */
  .small{left:376px;top:76px;width:404px;height:281px}
  .small .headline{left:14px;top:10px;font-family:"Roboto Condensed",sans-serif;font-weight:700;font-size:16px;line-height:18px;color:var(--white)}
  .small .intro{right:13px;top:20px;width:230px;text-align:right;font-size:8.5px;line-height:12px}
  .small .brand-name{right:13px;top:80px;font-size:19px}
  .small .photo{left:280px;top:120px;width:124px;height:161px;background:linear-gradient(160deg,#f29a3a 0%,#c9582a 45%,#6d2c18 100%)}
  .small .reputation{right:136px;top:115px;text-align:right;font-size:8.5px;line-height:12px;font-weight:700}
  .small .reviews{right:136px;top:145px;font-size:8px;letter-spacing:.2px}
  .small .divider{left:0;top:166px;width:268px;height:1px;background:#b7b7b7}
  .small .visit{right:136px;top:176px;text-align:right;font-size:11px;line-height:18px}
  .small .visit b{font-size:12px}
  .small .benefits-band{left:0;top:225px;width:280px;height:56px;background:linear-gradient(180deg,#f7f1e6 0%,var(--tan-light) 60%,#dccbaa 100%)}
  .small .benefits-title{left:14px;top:229px;font-size:14px;color:#4a4a4a;border-bottom:1px solid #4a4a4a;line-height:16px}
  .small .benefit-list{right:136px;top:228px;list-style:none;text-align:right;font-size:8.5px;font-weight:700;line-height:15px}
  .small .benefit-list li::after{content:"";display:inline-block;width:5px;height:5px;border-radius:50%;background:var(--navy);margin-left:8px;vertical-align:1px}

  /* half page flyer */
  .half{left:129px;top:431px;width:942px;height:665px}
  .half .brand-name{right:311px;top:62px;font-size:35px}
  .half .body-copy{left:44px;top:143px;width:590px;font-size:18.4px;line-height:29px;text-align:justify}
  .half .helps-title{left:44px;top:318px;font-family:"Arimo",sans-serif;font-weight:400;font-size:24px;color:var(--navy)}
  .half .helps-list{left:44px;top:368px;display:grid;grid-template-columns:180px 340px;row-gap:1px;list-style:none;font-size:17.5px;line-height:22px;white-space:nowrap}
  .half .helps-list li{padding-left:27px;position:relative}
  .half .helps-list li::before{content:"";position:absolute;left:2px;top:7px;width:9px;height:9px;background:var(--bullet)}
  .half .note{left:44px;top:428px;font-size:17px;white-space:nowrap}
  .half .call{left:179px;top:508px;font-family:"Arimo",sans-serif;color:var(--navy);font-size:26px;white-space:nowrap}
  .half .call b{font-family:"Roboto Condensed",sans-serif;font-size:40px;letter-spacing:.3px}
  .half .visit{left:44px;top:577px;font-family:"Arimo",sans-serif;color:var(--navy);font-size:22px;white-space:nowrap}
  .half .visit span{font-size:31px}
  .half .side-strip{right:0;top:0;width:46px;height:665px;background:linear-gradient(90deg,#f2f2f2,var(--silver))}
  .half .photo{left:680px;width:216px;box-shadow:3px 3px 6px rgba(0,0,0,.3)}
  .half .photo-treatment{top:0;height:289px;background:linear-gradient(160deg,#f3a640 0%,#d06a2c 40%,#7a301a 100%)}
  .half .photo-shoulder{top:309px;height:140px;background:radial-gradient(ellipse at 45% 45%,#e5dccd 0%,#a0927c 45%,#2d2923 100%)}
  .half .photo-spine{top:464px;height:144px;background:radial-gradient(ellipse at 50% 55%,#ece1cc 0%,#a48f6f 40%,#231d16 100%)}
</style>
</head>
<body>

<section class="flyer small" aria-label="Small flyer">
  <svg class="backdrop" width="404" height="281" viewBox="0 0 404 281" aria-hidden="true">
    <path d="M0 0 H404 V6 C260 20 90 55 0 128 Z" fill="var(--tan)"/>
    <path d="M0 0 H404 V0 C250 10 80 45 0 118 Z" fill="var(--orange)"/>
  </svg>
  <p class="abs headline">Feel better after the<br>First Session!</p>
  <p class="abs intro">Restore your body's<br>natural resiliency and greatly<br>reduce your physical pain through the<br>Dr. Mara Tessvik Method of Structural Integration</p>
  <p class="abs brand-name">Larch Tessvik Therapy</p>
  <div class="photo" role="img" aria-label="Photo of the practitioner working on a client's shoulders"></div>
  <p class="abs reputation">Our practitioner is highly experienced<br>and has a great reputation</p>
  <p class="abs reviews">VISIT OUR WEB SITE FOR REVIEWS</p>
  <div class="abs divider"></div>
  <p class="abs visit">Visit our web site <b>LarchTessvik.com</b><br><b>call 786-555 0148</b></p>
  <div class="abs benefits-band"></div>
  <p class="abs benefits-title">Benefits</p>
  <ul class="abs benefit-list">
    <li>Reduce aches and pains</li>
    <li>Reduce joint pain</li>
    <li>Reduce chronic muscular tension</li>
  </ul>
</section>

<section class="flyer half" aria-label="Half page flyer">
  <svg class="backdrop" width="942" height="665" viewBox="0 0 942 665" aria-hidden="true">
    <path d="M0 0 H430 C250 30 90 90 0 168 Z" fill="var(--tan)"/>
    <path d="M0 0 H404 C230 22 80 80 0 152 Z" fill="var(--orange)"/>
    <path d="M0 665 C320 640 700 560 942 486 V665 Z" fill="var(--tan)"/>
    <path d="M0 665 C340 652 700 585 942 515 V665 Z" fill="var(--orange)"/>
  </svg>
  <div class="abs side-strip"></div>
  <p class="abs brand-name">Larch Tessvik Therapy</p>
  <p class="abs body-copy">Control your weight (This part should be emphasized) by balancing your nervous and digestive system through the Tessvik Method. The Tessvik Method, a technique developed by Dr. Mara. Tessvik, uses physical pressure to manipulate visceral tissue to bring back resiliency and proper functioning of the whole body.</p>
  <h2 class="abs helps-title">Also helps with</h2>
  <ul class="abs helps-list">
    <li>Constipation</li>
    <li>Bloating</li>
    <li>IBS</li>
    <li>Eating disorders and overeating</li>
  </ul>
  <p class="abs note">Our practitioner is highly experienced. Please visit our web sites for reviews.</p>
  <p class="abs call">Call <b>786-555-0148</b></p>
  <p class="abs visit">Visit our web site <span>LarchTessvik.com</span></p>
  <div class="photo photo-treatment" role="img" aria-label="Photo of a practitioner pressing a client's upper back"></div>
  <div class="photo photo-shoulder" role="img" aria-label="Illustration of a shoulder and rib cage skeleton"></div>
  <div class="photo photo-spine" role="img" aria-label="Illustration of a back with the spine highlighted"></div>
</section>

</body>
</html>
```